Content services firm needs a new web banner and email signature graphic

UPDATE April 2:
I'm sharing a lumora stock board for inspiration. I don't want this to look like clip art. I'd like to capture the digital part of the theme better. The blocks are too boring.

https://www.lumorastock.example/collaboration/boards/-qR4Tx8WLMZkapHDnZeVoLw

We are running a campaign around microcontent. We need new web banner and email signature graphic. We have a current banner on the website, but we'd like to replace it. I'd also like a much smaller, but similarly themed graphic for our email signatures.

I have attached a mock-up pencil illustration and an image to provide some guidance. I am thinking a nice clean background with a dozens of little colourful cubes strewn across the background. The magnifying glass isolates one cube and we have the text on the side explaining microcontent.

I will try to add additional graphics for inspiration.

SIZE:
The main graphic is 1680 x 593 px
The email graphic is 400 x 100 px

Target Market(s)

Medium to large organizations trying to strategically leverage content assets.

Industry/Entity Type

Information Technology

Font styles to use
Sans Serif

Colors

Designer to choose colors to be used in the design.

Requirements
Must have
• Must be clean and bright.
• Must include the following text:
• The next big thing: Microcontent
• Digital transformation has forever changed customer expectations. Is your content ready for an omni-channel future?
• Microcontent is content that is
• • about one primary idea
• • easily scannable
• • titled for clear search and meaning, and
• • future-enabled for use anywhere and any time it is needed.
• It's not microcontent just because it's small.
• Click the cube to learn more.
Nice to have
• It would cool if the cube could be the button to learn more and if it were to change colour when hovered over. But this is critical and may be restricted by our web tech.
• I think we are using WordPress 4

```html
<!DOCTYPE html>
<html lang="en">
<head>
<meta charset="utf-8">
<title>The Next Big Thing: Microcontent</title>
<link rel="stylesheet" href="https://fonts.googleapis.com/css2?family=Audiowide&family=Jura:wght@400;500;600&family=Merriweather:ital,wght@0,400;1,400&display=swap">
<style>
  :root {
    --ink: #000000;
    --white: #ffffff;
    --cyan: #1ce6f2;
    --amber: #ffa31c;
    --glow-core: #4fd0ff;
    --glow-mid: #0d7fd8;
    --glow-deep: #0a2a63;
    --cta-top: #ff4a12;
    --cta-bottom: #d61800;
    --cube-top: #ff8a1a;
    --cube-bottom: #f04a00;
    --pill-idea-a: #8a16ff;
    --pill-idea-b: #d42cff;
    --pill-scan-a: #c42400;
    --pill-scan-b: #ff5200;
    --pill-title-a: #ff4e00;
    --pill-title-b: #ffc81a;
    --pill-future-a: #8a0f7a;
    --pill-future-b: #ff1f8e;
  }
  * { box-sizing: border-box; margin: 0; padding: 0; }
  html, body { width: 1200px; height: 424px; overflow: hidden; background: var(--ink); }
  .banner {
    position: relative;
    width: 1200px;
    height: 424px;
    overflow: hidden;
    background: var(--ink);
    font-family: "Jura", sans-serif;
    color: var(--white);
  }
  .tech-backdrop {
    position: absolute;
    left: 330px;
    top: 0;
    width: 870px;
    height: 424px;
    background:
      radial-gradient(circle at 404px 238px, rgba(255,255,255,0.55) 0 60px, rgba(150,225,255,0.35) 96px, transparent 100px),
      radial-gradient(circle at 404px 238px, var(--glow-core) 0, var(--glow-mid) 160px, var(--glow-deep) 300px, var(--ink) 470px);
  }
  .tech-backdrop::after {
    content: "";
    position: absolute;
    inset: 0;
    background: linear-gradient(90deg, var(--ink) 0, rgba(0,0,0,0) 180px, rgba(0,0,0,0) 620px, rgba(0,0,0,0.55) 870px);
  }
  .headline {
    position: absolute;
    left: 67px;
    top: 62px;
    font-family: "Audiowide", sans-serif;
    font-size: 28px;
    line-height: 30px;
    letter-spacing: 0.5px;
    text-transform: uppercase;
  }
  .headline-lead { display: block; color: var(--cyan); }
  .headline-key { display: block; color: var(--amber); }
  .intro {
    position: absolute;
    left: 65px;
    top: 162px;
    width: 400px;
    font-size: 20px;
    font-weight: 500;
    line-height: 25px;
  }
  .cta {
    position: absolute;
    left: 64px;
    top: 336px;
    width: 246px;
    height: 34px;
    border-radius: 17px;
    background: linear-gradient(var(--cta-top), var(--cta-bottom));
    box-shadow: 0 0 8px rgba(255,60,0,0.6);
    font-family: "Merriweather", serif;
    font-style: italic;
    font-size: 15px;
    line-height: 34px;
    text-align: center;
    color: var(--white);
  }
  .cube-note {
    position: absolute;
    left: 684px;
    top: 180px;
    width: 96px;
    height: 96px;
    padding-top: 10px;
    background: linear-gradient(160deg, var(--cube-top), var(--cube-bottom));
    transform: rotate(6deg);
    font-family: "Merriweather", serif;
    font-size: 11px;
    line-height: 14px;
    text-align: center;
    color: var(--white);
  }
  .definition {
    position: absolute;
    left: 896px;
    top: 52px;
    font-family: "Audiowide", sans-serif;
    font-size: 19px;
    line-height: 25px;
    text-transform: uppercase;
  }
  .traits { list-style: none; }
  .trait {
    position: absolute;
    display: flex;
    align-items: center;
    padding-left: 22px;
    border-radius: 24px 24px 24px 24px;
    font-size: 14.5px;
    font-weight: 500;
    line-height: 15px;
  }
  .trait-idea { left: 868px; top: 122px; width: 148px; height: 47px; background: linear-gradient(90deg, var(--pill-idea-a), var(--pill-idea-b)); }
  .trait-scan { left: 902px; top: 181px; width: 124px; height: 47px; padding-left: 19px; background: linear-gradient(90deg, var(--pill-scan-a), var(--pill-scan-b)); }
  .trait-title { left: 912px; top: 238px; width: 196px; height: 48px; padding-left: 10px; background: linear-gradient(90deg, var(--pill-title-a), var(--pill-title-b)); }
  .trait-future { left: 890px; top: 298px; width: 238px; height: 58px; padding-left: 7px; background: linear-gradient(90deg, var(--pill-future-a), var(--pill-future-b)); }
</style>
</head>
<body>
  <section class="banner">
    <div class="tech-backdrop" role="img" aria-label="Glowing blue digital rings with floating cubes and a magnifying glass isolating one orange cube"></div>

    <h1 class="headline">
      <span class="headline-lead">The next big thing :</span>
      <span class="headline-key">Microcontent</span>
    </h1>

    <p class="intro">Digital transformation has forever changed customer expectations Is your content ready for an omni channel future</p>

    <a class="cta">Click the cube to learn more</a>

    <p class="cube-note">It's not<br>Microcontent<br>just because<br>it's small</p>

    <h2 class="definition">Microcontent is<br>content that is</h2>

    <ul class="traits">
      <li class="trait trait-idea">About one<br>primary idea</li>
      <li class="trait trait-scan">Easily<br>scannable</li>
      <li class="trait trait-title">Titled for clear<br>search and meaning</li>
      <li class="trait trait-future">Future-enabled for use<br>anywhere &amp; any time it is<br>needed</li>
    </ul>
  </section>
</body>
</html>
```